Vostrel Holdings Web Design

Vostrel Holdings Limited Shenzhen

This project is a 10 page launch website.
Our client is seeking a contemporary homepage design for a Holdings company. Once we are happy with the homepage design and select designer we will request a secondary page design.

Please see attached company LOGO for an idea of style, it incorporates the traditional Chinese furniture lattice work. The Quillmoor website is one of our clients favorite so we would like to see a similar homepage design to this website.

Use the websites below for reference purpose. The first two are Chinese and the second two are international. We would like to see elements of both but more focus on international design.

http://www.evergrande.com/http://www.brevandgroup.com/pub/default.aspx http://www.quillmoor.com/zh/maldives_resortone/
http://www.vellune-studio.com
http://media-cache-ec0.fotrelix.com/originals/41/a3/90/41a390c1f5b7d2e8a6c4f0b9e3d71a55.jpg

Company Background
VOSTREL HOLDINGS, located in Qianhai, China, is a new real-estate project operator, structuring urban-rural real-estate investment and development, and industrial fund investment. The company also invests in supply chain management and supporting infrastructures. To create new spaces and livable cities Vostrel Holdings develop win-win strategic partnerships with a number of institutions. Currently cooperating with Harrow East Lindcombe, China urban and rural integrated demonstration.

Target Market(s)

B2B property investment. Target market customers are senior level management/decision makers of large corporations. Focusing geographically on the domestic market first and expanding internationally in 2nd and 3rd years.

Industry/Entity Type

Investment

Requirements
Must have
• Since this is a new company, we would like to the website representing growth and power, E.g. like a growing tree.
Should not have
• Low-level vectors such as curency symbols, American dollar.

```html
<!DOCTYPE html>
<html lang="en">
<head>
<meta charset="utf-8">
<title>Vostrel Holdings</title>
<link href="https://fonts.googleapis.com/css2?family=Open+Sans:wght@300;400;600;700&display=swap" rel="stylesheet">
<style>
:root{
  --topbar:#818284;
  --slate:#6d6e72;
  --gold:#c0a04c;
  --gold-soft:#e0d1a7;
  --field:#f2ecdc;
  --white:#ffffff;
  --text:#f1f1f1;
}
*{box-sizing:border-box;margin:0;padding:0}
html,body{width:1200px;height:1164px;overflow:hidden;background:var(--slate)}
body{font-family:"Open Sans",Arial,sans-serif;color:var(--text);position:relative}
.topbar{position:absolute;left:0;top:0;width:1200px;height:90px;background:var(--topbar);border-bottom:1px solid var(--gold)}
.header{position:absolute;left:0;top:91px;width:1200px;height:179px;background:var(--slate)}
.brand{position:absolute;left:66px;top:27px;width:150px;text-align:center}
.brand-mark{display:block;width:84px;height:84px;margin:0 auto 8px;border:2px solid var(--gold);border-radius:50%}
.brand-name{font-size:16px;font-weight:400;color:var(--gold);letter-spacing:.3px;white-space:nowrap}
.search-field{position:absolute;left:556px;top:45px;width:381px;height:46px;background:var(--field);border:3px solid var(--gold);border-radius:4px}
.search-button{position:absolute;left:947px;top:45px;width:189px;height:46px;border-radius:4px;overflow:hidden;background:linear-gradient(to bottom,var(--gold-soft) 0,var(--gold-soft) 40%,var(--gold) 40%);display:flex;align-items:center;justify-content:center;gap:12px;color:var(--white);font-size:20px;font-weight:400}
.nav{position:absolute;left:273px;top:143px;width:863px;display:flex;justify-content:space-between;list-style:none}
.nav li{font-size:15px;color:var(--white);white-space:nowrap}
.hero{position:absolute;left:0;top:270px;width:1200px;height:435px;background:linear-gradient(to bottom,#c9dcef 0%,#dde8f1 30%,#6f9a4a 55%,#3f6b2e 75%,#7a8a4c 100%)}
.hero-title{position:absolute;left:66px;top:50px;font-size:26px;font-weight:400;color:var(--gold)}
.hero-sub{position:absolute;left:66px;top:86px;font-size:14px;color:var(--gold)}
.intro{position:absolute;left:64px;top:736px;width:650px;font-size:14px;line-height:21.7px;color:var(--text)}
.intro p{margin-bottom:22px}
.intro strong{font-weight:700;color:var(--white)}
.tiles{position:absolute;left:64px;top:957px;display:flex;gap:13px}
.tile{position:relative;width:206px;height:98px;border-radius:5px;overflow:hidden;background:var(--gold)}
.tile svg{position:absolute;left:0;top:0}
.tile-label{position:absolute;left:0;top:24px;width:100%;text-align:center;font-size:20px;font-weight:300;line-height:28px;color:var(--white)}
.divider{position:absolute;left:779px;top:740px;width:1px;height:351px;background:var(--gold)}
.contact{position:absolute;left:802px;top:733px;width:334px}
.contact h2{font-size:26px;font-weight:400;color:var(--gold);margin-bottom:4px}
.contact p{font-size:14px;line-height:20.5px;color:var(--text)}
.contact .gap{margin-top:20px}
.rule{height:1px;background:var(--gold);margin:14px 0 12px}
.contact h3{font-size:23px;font-weight:400;color:var(--white);margin-bottom:2px}
.links{list-style:none;margin-top:18px}
.links li{font-size:14px;line-height:20.5px;color:var(--gold)}
.footer{position:absolute;left:0;top:1121px;width:1200px;height:43px;background:var(--gold);display:flex;justify-content:center;align-items:center;gap:9px}
.social{width:26px;height:26px;border:2px solid var(--white);border-radius:50%}
</style>
</head>
<body>
<div class="topbar"></div>
<header class="header">
  <div class="brand"><span class="brand-mark"></span><span class="brand-name">Vostrel Holdings</span></div>
  <div class="search-field"></div>
  <div class="search-button">
    <svg width="30" height="30" viewBox="0 0 30 30" aria-hidden="true"><circle cx="15" cy="15" r="13" fill="none" stroke="#fff" stroke-width="2"/><circle cx="13.5" cy="13.5" r="4.5" fill="none" stroke="#fff" stroke-width="2"/><line x1="17" y1="17" x2="21" y2="21" stroke="#fff" stroke-width="2.4" stroke-linecap="round"/></svg>
    <span>SEARCH</span>
  </div>
  <ul class="nav">
    <li>HOME</li><li>ABOUT VOSTREL HOLDINGS</li><li>NEWS CENTER</li><li>OUR PROJECTS</li><li>GROUP BUSINESS</li><li>CORPORATE CULTURE</li><li>CONTACT US</li>
  </ul>
</header>
<section class="hero" role="img" aria-label="Chinese garden with a red pavilion, a large rock and willow trees beside a calm lake">
  <h1 class="hero-title">Vostrel Holdings</h1>
  <p class="hero-sub">Lorem ipsum dolor sit amet, consectetur adipiscing elit</p>
</section>
<section class="intro">
  <p><strong>VOSTREL HOLDINGS</strong> located in Qianhai, China, is a new real-estate project operator, structuring urban-rural real-estate investment and development, and industrial fund investment.</p>
  <p>The company also invests in supply chain management and supporting infrastructures.<br>To create new spaces and livable cities Vostrel Holdings develop win-win strategic partnerships with a number of institutions. Currently cooperating with Harrow East Lindcombe, China urban and rural integrated demonstration.</p>
</section>
<div class="tiles">
  <div class="tile"><svg width="206" height="98" viewBox="0 0 206 98" aria-hidden="true"><path d="M0 0H206V42Q103 26 0 46Z" fill="#e0d1a7"/></svg><div class="tile-label">LOREM IPSUM<br>DOLOR</div></div>
  <div class="tile"><svg width="206" height="98" viewBox="0 0 206 98" aria-hidden="true"><path d="M0 0H206V42Q103 26 0 46Z" fill="#e0d1a7"/></svg><div class="tile-label">LOREM IPSUM<br>DOLOR</div></div>
  <div class="tile"><svg width="206" height="98" viewBox="0 0 206 98" aria-hidden="true"><path d="M0 0H206V42Q103 26 0 46Z" fill="#e0d1a7"/></svg><div class="tile-label">LOREM IPSUM<br>DOLOR</div></div>
</div>
<div class="divider"></div>
<aside class="contact">
  <h2>Contact Information</h2>
  <p>Suite 123, Address Road Boulevard<br>Qianhai, China</p>
  <p class="gap">Tel +0755 987 6543<br>Fax +0755 987 6543<br>E-mail info@vostrelholdings.com</p>
  <div class="rule"></div>
  <h3>Lorem ipsum dolor sit amet,</h3>
  <p>consectetur adipiscing elit.<br>Nam non malesuada enim. Suspendisse potenti.</p>
  <ul class="links">
    <li>About Vostrel Holdings</li><li>Architecture</li><li>Corporate Social Responsibility</li><li>Meet the General Manager</li>
  </ul>
</aside>
<footer class="footer">
  <span class="social" aria-label="Social link"></span>
  <span class="social" aria-label="Social link"></span>
  <span class="social" aria-label="Social link"></span>
  <span class="social" aria-label="Social link"></span>
</footer>
</body>
</html>
```